It's a new electrical company based in Newcastle NSW. I would like a logo between the two words "BRYN (insert logo) VOLT". I would like the logo to represent electrical and celtic style. For example I have seen a light bulb with a celtic pattern in the middle which looked very good. I would like it to be a white card, mainly black writing and quite basic not too much going on. But maybe have the logo partially red or green?

BRYN VOLT
Electrical Contractors
Domestic, commercial, fault finding, testing, re wires, switchboard upgrades
License No: 738421K
Fully Insured
Phone: 0431587720

```html
<!DOCTYPE html>
<html lang="en">
<head>
<meta charset="utf-8">
<title>Bryn Volt – Business Card</title>
<link href="https://fonts.googleapis.com/css2?family=Source+Sans+3:wght@400;600&display=swap" rel="stylesheet">
<style>
  :root {
    --backdrop: #000000;
    --card: #ffffff;
    --ink: #231f20;
    --teal: #0e98b3;
    --teal-mid: #4cb3c8;
    --teal-light: #8fcadb;
  }
  html, body {
    margin: 0;
    padding: 0;
    width: 1200px;
    height: 900px;
    overflow: hidden;
    background: var(--backdrop);
  }
  .canvas {
    position: relative;
    width: 1200px;
    height: 900px;
    background: var(--backdrop);
  }
  .business-card {
    position: absolute;
    left: 173px;
    top: 194px;
    width: 852px;
    height: 507px;
    background: var(--card);
    overflow: hidden;
    font-family: "Source Sans 3", sans-serif;
  }
  .corner-swoosh {
    position: absolute;
    left: 0;
    top: 0;
    width: 852px;
    height: 507px;
  }
  .brand {
    position: absolute;
    left: 0;
    right: 0;
    top: 109px;
    height: 114px;
    display: flex;
    align-items: center;
    justify-content: center;
    gap: 22px;
    color: var(--ink);
    font-size: 46px;
    font-weight: 600;
    letter-spacing: 6px;
  }
  .brand-mark {
    width: 108px;
    height: 108px;
    border: 3px solid var(--teal);
    border-radius: 50%;
    box-sizing: border-box;
  }
  .wire-divider {
    position: absolute;
    left: 195px;
    top: 276px;
    width: 472px;
    height: 24px;
  }
  .services {
    position: absolute;
    left: 0;
    right: 0;
    top: 345px;
    text-align: center;
    color: var(--teal);
    font-size: 21px;
    line-height: 26.5px;
  }
  .services .trade {
    color: var(--ink);
    font-size: 27px;
    line-height: 34px;
    margin: 0 0 2px;
    font-weight: 400;
  }
  .services p {
    margin: 0;
  }
</style>
</head>
<body>
<div class="canvas">
  <section class="business-card">
    <svg class="corner-swoosh" viewBox="0 0 852 507" aria-hidden="true">
      <path d="M0 0 H245 C130 60 30 200 0 395 Z" fill="var(--teal-light)"/>
      <path d="M0 0 H205 C110 60 30 165 0 305 Z" fill="var(--teal-mid)"/>
      <path d="M0 0 H168 C90 55 25 130 0 232 Z" fill="var(--teal)"/>
      <path d="M852 507 V325 C820 400 770 460 710 507 Z" fill="var(--teal-light)"/>
      <path d="M852 507 V362 C825 420 785 470 742 507 Z" fill="var(--teal-mid)"/>
      <path d="M852 507 V398 C830 445 800 480 772 507 Z" fill="var(--teal)"/>
    </svg>

    <div class="brand">
      <span class="brand-word">BRYN</span>
      <span class="brand-mark"></span>
      <span class="brand-word">VOLT</span>
    </div>

    <svg class="wire-divider" viewBox="0 0 472 24" aria-hidden="true">
      <path d="M8 12 H205 C212 12 214 20 220 20 S228 4 235 4 S243 20 250 20 S258 12 265 12 H464"
            fill="none" stroke="var(--teal)" stroke-width="2.5"/>
      <circle cx="8" cy="12" r="6.5" fill="var(--teal)"/>
      <circle cx="464" cy="12" r="6.5" fill="var(--teal)"/>
    </svg>

    <div class="services">
      <h2 class="trade">Electrical Contractors</h2>
      <p>Domestic, commercial, fault finding, testing,</p>
      <p>re wires, switchboard upgrades</p>
      <p>License No: 738421K Fully Insured Phone: 0431587720</p>
    </div>
  </section>
</div>
</body>
</html>
```